Business Card Design using new logo

As much as we'd like to think that treating everyone equally is the best strategy for fairness, the reality is that the differences in the lives of women and men have to be taken into account to ensure that organizations, programs, services, and yes, even public policy treat women and men in ways that achieve gender equity.

That's where ParityLumen - fairness metrics insight comes in. Using the data-driven tools of gender analysis, our organization can help anyone determine if gender equity is being achieved - in businesses and organizations, in the planning and implementation of programs and services, and in the development and enforcement of public policy.
Updates

Apologies for the delay - have not had time to finalize the decision.  Should be early this week - probably Tuesday.

Industry/Entity Type

Business

Requirements
Must have
• New Logo for ParityLumen
• Logo plus words "Fairness Metrics Insight"

```html
<!DOCTYPE html>
<html lang="en">
<head>
<meta charset="utf-8">
<title>ParityLumen – Business Card</title>
<link href="https://fonts.googleapis.com/css2?family=Open+Sans:wght@400;600;700&display=swap" rel="stylesheet">
<style>
  :root {
    --stage: #666666;
    --card-dark-top: #7a7a7a;
    --card-dark-bottom: #3c3c3c;
    --card-light: #ffffff;
    --accent: #f5821f;
    --accent-soft: #fdd7a6;
    --ink: #222222;
    --ink-mid: #4a4a4a;
    --ink-soft: #666666;
    --rule: #333333;
    --white: #ffffff;
  }
  * { box-sizing: border-box; margin: 0; padding: 0; }
  html, body { width: 1200px; height: 999px; overflow: hidden; }
  body {
    background: var(--stage);
    font-family: "Open Sans", Arial, sans-serif;
    position: relative;
  }
  .card {
    position: absolute;
    top: 355px;
    width: 500px;
    height: 286px;
    overflow: hidden;
  }
  .brand-dot {
    border-radius: 50%;
    background: var(--accent);
    flex: none;
  }
  .brand-text { display: flex; flex-direction: column; }
  .brand-name {
    font-weight: 600;
    letter-spacing: -0.5px;
    line-height: 1.1;
    white-space: nowrap;
  }
  .brand-tagline {
    font-weight: 400;
    text-transform: uppercase;
    white-space: nowrap;
  }

  /* Front */
  .card-front {
    left: 80px;
    background: radial-gradient(ellipse at 30% 15%, var(--card-dark-top), var(--card-dark-bottom) 80%);
  }
  .front-brand {
    position: absolute;
    left: 0; right: 0; top: 104px;
    display: flex; align-items: center; justify-content: center; gap: 14px;
  }
  .front-brand .brand-dot { width: 34px; height: 34px; }
  .front-brand .brand-name { color: var(--white); font-size: 40px; }
  .front-brand .brand-tagline {
    color: var(--white);
    font-size: 11px; letter-spacing: 2.4px; margin-top: 4px; padding-left: 2px;
  }
  .front-web {
    position: absolute; right: 26px; bottom: 22px;
    color: var(--white);
    font-size: 12px; letter-spacing: 3px;
  }

  /* Back */
  .card-back {
    left: 620px;
    background: var(--card-light);
  }
  .back-decor {
    position: absolute;
    left: -80px; top: 40px;
    width: 220px; height: 220px;
  }
  .back-brand {
    position: absolute; right: 32px; top: 44px;
    display: flex; align-items: center; gap: 10px;
  }
  .back-brand .brand-dot { width: 28px; height: 28px; }
  .back-brand .brand-name { color: var(--ink); font-size: 30px; }
  .back-brand .brand-tagline {
    color: var(--ink-soft);
    font-size: 8.5px; letter-spacing: 1.9px; margin-top: 3px; padding-left: 1px;
  }
  .person {
    position: absolute; left: 305px; top: 142px;
  }
  .person-name {
    color: var(--ink-mid);
    font-size: 17px; font-weight: 700; letter-spacing: 0.3px;
  }
  .person-role {
    color: var(--ink-soft);
    font-size: 11.5px; margin-top: 1px;
  }
  .contacts {
    list-style: none; margin-top: 14px;
    color: var(--ink-soft);
    font-size: 12px; line-height: 18px;
  }
  .contacts li { display: flex; align-items: center; gap: 9px; }
  .contacts svg { width: 11px; height: 11px; flex: none; }
  .square-mark {
    width: 10px; height: 10px; background: var(--ink-mid); flex: none;
  }
  .back-rule {
    position: absolute; left: 0; bottom: 14px;
    width: 290px; height: 7px; background: var(--rule);
  }
  .back-web {
    position: absolute; left: 305px; bottom: 12px;
    color: var(--ink-mid);
    font-size: 12px; font-weight: 600; letter-spacing: 2.6px;
  }
</style>
</head>
<body>

  <section class="card card-front" aria-label="Business card front">
    <div class="front-brand">
      <span class="brand-dot"></span>
      <div class="brand-text">
        <span class="brand-name">ParityLumen</span>
        <span class="brand-tagline">Fairness Metrics Insight</span>
      </div>
    </div>
    <p class="front-web">www.paritylumen.com</p>
  </section>

  <section class="card card-back" aria-label="Business card back">
    <svg class="back-decor" viewBox="0 0 220 220" aria-hidden="true">
      <circle cx="110" cy="110" r="110" fill="var(--accent-soft)" opacity="0.55"/>
    </svg>

    <div class="back-brand">
      <span class="brand-dot"></span>
      <div class="brand-text">
        <span class="brand-name">ParityLumen</span>
        <span class="brand-tagline">Fairness Metrics Insight</span>
      </div>
    </div>

    <div class="person">
      <h1 class="person-name">PERSON NAME</h1>
      <p class="person-role">your designation</p>
      <ul class="contacts">
        <li>
          <svg viewBox="0 0 12 12" aria-hidden="true"><rect x="0.5" y="2" width="11" height="8" fill="none" stroke="#4a4a4a"/><path d="M0.5 2 L6 7 L11.5 2" fill="none" stroke="#4a4a4a"/></svg>
          person@paritylumen.com
        </li>
        <li><span class="square-mark"></span>facebook.com/paritylumen</li>
        <li>
          <svg viewBox="0 0 12 12" aria-hidden="true"><path d="M3 1 L5 3.5 L4 5 Q5 7 7 8 L8.5 7 L11 9 L9.5 11 Q5 11 2.5 7.5 Q1 5 1.5 2.5 Z" fill="#4a4a4a"/></svg>
          00-000-0000
        </li>
      </ul>
    </div>

    <div class="back-rule"></div>
    <p class="back-web">www.paritylumen.com</p>
  </section>

</body>
</html>
```